Project Title:
Dental Implant Overdenture Flyer (Retirement Village Target)
Objective:
Create a clean, trustworthy, and reassuring flyer aimed at older adults (60–85 years old) who struggle with loose dentures. The goal is to educate them about implant-retained “clip-on” dentures and encourage them to book a consultation.
Tone & Feel:
Warm, caring, non-intimidating
Premium but not “salesy”
Medical but easy to understand
Focus on improving quality of life (confidence, eating, comfort)
Target Audience:
Retirees / pensioners
Existing denture wearers
People frustrated with loose or uncomfortable dentures
Key Message:
“You don’t have to live with loose dentures anymore.”
Design Style:
Clean, minimal, modern
Soft colours (blues, greens, warm neutrals)
Easy-to-read large font
High contrast for older eyes
Avoid clutter
Imagery Suggestions:
Smiling older adults (natural, not stocky/overly staged)
Before/after lifestyle (eating, laughing, socialising)
Simple diagram showing denture clipping onto implants
Avoid graphic surgical images
Layout Suggestions:
A5 or DL flyer
Clear sections with headings
Icons for benefits
Strong call-to-action at bottom
HEADLINE (big and bold)
Tired of Loose Dentures?
Discover Secure “Clip-On” Teeth
🔹 PROBLEM SECTION
Do your dentures:
Slip or move when eating?
Make it hard to chew certain foods?
Feel uncomfortable or loose?
Affect your confidence when speaking or smiling?
You’re not alone — and there is a better solution.
🔹 SOLUTION SECTION
Implant-Retained “Clip-On” Dentures
We can secure your denture using just 2 dental implants, allowing your teeth to:
✔ Stay firmly in place
✔ Improve your ability to eat
✔ Feel more comfortable
✔ Boost your confidence
🔹 SIMPLE EXPLANATION (very important)
Small titanium implants are gently placed in the jaw.
Your denture then clips securely onto them, stopping movement.
🔹 PRICE SECTION (highlight this clearly)
$12,000
Includes:
2 dental implants
A brand new custom overdenture
Does not include sedation or extractions (if needed)
🔹 SEDATION
Sedation is available for comfort.
If you hold a pensioner card, you may receive a significant Vantacor rebate, often resulting in minimal out-of-pocket costs for sedation.
🔹 TRUST / REASSURANCE
Experienced implant clinician
Gentle, patient-focused care
Modern technology and techniques
🔹 CALL TO ACTION (VERY IMPORTANT)
Book a Free Consultation
📞 Call: 08 9351 4276
🌐 Visit: www.bravonclinic.com.au
📍 Located near Tallowmere shopping centre
🔹 OPTIONAL TAGLINE
Eat Better. Feel Better. Smile with Confidence Again.
Please include some photos to illustrate what a clip on denture looks like with two implants.

```html
<!DOCTYPE html>
<html lang="en">
<head>
<meta charset="utf-8">
<title>Clip-On Dentures Flyer</title>
<link rel="stylesheet" href="https://fonts.googleapis.com/css2?family=Poppins:wght@400;500;600;700;800&display=swap">
<style>
:root{
  --backdrop:#b5b5b5;
  --navy:#0d4f80;
  --deep:#0f6189;
  --teal:#10b6c8;
  --sky:#7fdcf5;
  --ink:#111418;
  --white:#ffffff;
  --band:#0a86b8;
}
*{margin:0;padding:0;box-sizing:border-box}
html,body{width:958px;height:1200px;overflow:hidden}
body{background:var(--backdrop);font-family:'Poppins',sans-serif;color:var(--ink);position:relative}
.flyer{position:absolute;left:107px;top:68px;width:744px;height:1054px;background:var(--white);overflow:hidden;box-shadow:6px 6px 8px rgba(0,0,0,.35)}

.hero{position:absolute;left:0;top:0;width:744px;height:358px;background:linear-gradient(100deg,#d9f6fd 0%,#b8eefb 45%,#6fd5f4 100%)}
.hero-photo{position:absolute;left:263px;top:40px;width:481px;height:318px;background:linear-gradient(110deg,rgba(233,238,242,0) 0%,rgba(233,238,242,.9) 22%,#f1b24a 48%,#c9d7ef 70%,#8ab0e6 100%);border-radius:90px 0 0 0}
.brand{position:absolute;left:42px;top:56px;display:flex;align-items:center;gap:8px}
.brand-mark{width:22px;height:22px;border-radius:50%;background:var(--deep)}
.brand-name{font-size:16px;font-weight:600;color:var(--deep);line-height:1.2;letter-spacing:1px}
.headline{position:absolute;left:39px;top:120px}
.headline .lead{font-size:36px;font-weight:400;line-height:40px;letter-spacing:1px}
.headline .big{font-size:47px;font-weight:800;color:var(--navy);line-height:41px;margin-top:1px}
.dots{position:absolute;left:41px;top:255px;display:flex;gap:3px}
.dots span{width:8px;height:8px;border-radius:50%;background:var(--teal)}
.dots span:nth-child(4){opacity:.6}
.dots span:nth-child(5){opacity:.25;width:4px}
.subhead{position:absolute;left:40px;top:272px;font-size:25px;line-height:28px}
.subhead b{font-weight:600}

.box{position:absolute;left:47px;width:319px;border-radius:16px;overflow:hidden;color:var(--white)}
.box-head{height:49px;padding:14px 26px 0;font-size:20px;font-weight:800;color:var(--navy)}
.problem{top:378px;height:205px;background:var(--deep)}
.problem .box-head{background:linear-gradient(90deg,#7fdcf5 0%,#3fa9cf 55%,var(--deep) 80%)}
.solution{top:594px;height:224px;background:var(--teal)}
.solution .box-head{background:linear-gradient(90deg,#8ee4f6 0%,#4fd0e6 60%,var(--teal) 90%)}
.box-title{font-size:17px;font-weight:800;padding:10px 26px 2px;line-height:1.3}
.solution .box-title{font-size:17.5px;padding-top:12px;line-height:1.28}
.solution p{font-size:11px;font-weight:500;padding:4px 16px 0 26px;line-height:1.25}
.ticks{list-style:none;padding:0 26px}
.ticks li{position:relative;padding-left:18px;font-size:12.5px;font-weight:500;line-height:1.35;margin-top:7px}
.benefits{display:grid;grid-template-columns:134px 150px;padding:8px 0 0 26px;row-gap:5px}
.benefits div{position:relative;padding-left:16px;font-size:11.5px;font-weight:500;line-height:1.3}
.ticks svg,.benefits svg,.col svg{position:absolute;left:0;top:3px}

.price{position:absolute;left:410px;top:372px;font-size:54px;font-weight:800;color:var(--navy);line-height:1}
.col{position:absolute;left:412px;width:285px;list-style:none}
.col li{position:relative;padding-left:16px}
.explain{top:440px}
.explain li{font-size:14.5px;font-weight:500;line-height:18px;margin-bottom:8px}
.tag{position:absolute;left:412px;width:103px;height:22px;border-radius:4px;background:var(--sky);color:var(--navy);font-size:15px;font-weight:600;padding-left:14px;line-height:23px}
.includes-tag{top:533px}
.sedation-tag{top:606px}
.includes{top:561px;display:flex}
.includes li{font-size:12px;font-weight:500;line-height:12px}
.includes .inc-denture{width:120px}
.includes .inc-denture span{display:block;width:82px}
.includes .inc-implants{width:160px}
.includes small{display:block;font-size:8.5px;font-weight:400;margin-top:3px;line-height:1.2}
.sedation{top:636px;width:280px}
.sedation li{font-size:12px;font-weight:400;line-height:14.5px;margin-bottom:8px}
.trust-title{position:absolute;left:412px;top:732px;font-size:21px;font-weight:800;color:var(--navy);line-height:1.2}
.trust{top:763px}
.trust li{font-size:12.5px;font-weight:400;line-height:17.8px}

.doctor-photo{position:absolute;left:37px;top:845px;width:155px;height:209px;background:linear-gradient(180deg,#f2f6f8 0%,#d8a888 40%,#1e1e1e 70%,#151515 100%);border-radius:40px 40px 0 0}
.doctor{position:absolute;left:192px;top:845px}
.doctor h2{font-size:24px;font-weight:700;color:var(--navy);line-height:1}
.doctor .role{font-size:15px;margin-top:2px}
.doctor p{font-size:11.5px;line-height:1.25;margin-top:12px;width:200px}
.mini{position:absolute;top:844px;width:135px;height:110px;border-radius:10px}
.mini-denture{left:413px;background:linear-gradient(135deg,#e3ecf3 0%,#b8c8d8 50%,#223a5c 100%)}
.mini-shade{left:559px;background:linear-gradient(135deg,#d9e4ec 0%,#c99a86 50%,#6a6fc2 100%)}

.cta-tab{position:absolute;left:192px;top:968px;width:254px;height:31px;background:var(--deep);clip-path:polygon(0 0,93% 0,100% 100%,0 100%);color:var(--white);font-size:15.5px;font-weight:600;padding:5px 0 0 18px}
.contact{position:absolute;left:184px;top:998px;width:560px;height:56px;background:var(--band);color:var(--white);display:flex;align-items:center;gap:12px;padding:6px 0 0 26px;font-size:13px}
.contact span{display:flex;align-items:center;gap:5px;white-space:nowrap}
.contact .near{position:relative}
.contact .near em{position:absolute;left:12px;top:-13px;font-style:normal;font-size:10px}
.on-white{color:#fff}
.on-ink{color:var(--ink)}
</style>
</head>
<body>
<svg width="0" height="0" style="position:absolute">
  <defs>
    <symbol id="tick" viewBox="0 0 12 12"><circle cx="6" cy="6" r="6" fill="#0d4f80"/><path d="M3.3 6.2l1.8 1.8 3.6-3.7" stroke="#fff" stroke-width="1.6" fill="none" stroke-linecap="round"/></symbol>
    <symbol id="tick-w" viewBox="0 0 12 12"><circle cx="6" cy="6" r="6" fill="#fff"/><path d="M3.3 6.2l1.8 1.8 3.6-3.7" stroke="currentColor" stroke-width="1.6" fill="none" stroke-linecap="round"/></symbol>
  </defs>
</svg>
<main class="flyer">
  <header class="hero">
    <div class="hero-photo" role="img" aria-label="Smiling older couple beside a large white tooth and implant model with dental mirror"></div>
    <div class="brand"><span class="brand-mark"></span><span class="brand-name">BRAVON<br>DENTAL SURGERY</span></div>
    <h1 class="headline"><div class="lead">Tired of</div><div class="big">LOOSE<br>DENTURES?</div></h1>
    <div class="dots"><span></span><span></span><span></span><span></span><span></span></div>
    <div class="subhead">Discover Secure<br><b>“Clip-On” Teeth</b></div>
  </header>

  <section class="box problem">
    <div class="box-head">PROBLEM</div>
    <div class="box-title">DO YOUR DENTURES</div>
    <ul class="ticks" style="color:var(--deep)">
      <li><svg width="11" height="11"><use href="#tick-w"/></svg><span class="on-white">Slip or move when eating?</span></li>
      <li><svg width="11" height="11"><use href="#tick-w"/></svg><span class="on-white">Make it hard to chew certain foods?</span></li>
      <li><svg width="11" height="11"><use href="#tick-w"/></svg><span class="on-white">Feel uncomfortable or loose?</span></li>
      <li><svg width="11" height="11"><use href="#tick-w"/></svg><span class="on-white">Affect your confidence when speaking or smiling?</span></li>
    </ul>
  </section>

  <section class="box solution">
    <div class="box-head">SOLUTION</div>
    <div class="box-title">IMPLANT-RETAINED<br>“CLIP-ON” DENTURES</div>
    <p>We can secure your denture using just 2 dental implants, allowing your teeth to</p>
    <div class="benefits" style="color:var(--teal)">
      <div><svg width="11" height="11"><use href="#tick-w"/></svg><span class="on-white">Stay firmly in place</span></div>
      <div><svg width="11" height="11"><use href="#tick-w"/></svg><span class="on-white">Feel more<br>comfortable</span></div>
      <div><svg width="11" height="11"><use href="#tick-w"/></svg><span class="on-white">Improve your<br>ability to eat</span></div>
      <div><svg width="11" height="11"><use href="#tick-w"/></svg><span class="on-white">Boost your confidence</span></div>
    </div>
  </section>

  <div class="price">$12,000</div>
  <ul class="col explain">
    <li><svg width="11" height="11"><use href="#tick"/></svg><span class="on-ink">Small titanium implants are gently placed in the jaw.</span></li>
    <li><svg width="11" height="11"><use href="#tick"/></svg><span class="on-ink">Your denture then clips securely onto them, stopping movement.</span></li>
  </ul>
  <div class="tag includes-tag">Includes</div>
  <ul class="col includes">
    <li class="inc-denture"><svg width="11" height="11"><use href="#tick"/></svg><span class="on-ink">A brand new custom overdenture</span></li>
    <li class="inc-implants"><svg width="11" height="11"><use href="#tick"/></svg><span class="on-ink">2 dental implants<small>Does not include sedation or extractions (if needed)</small></span></li>
  </ul>
  <div class="tag sedation-tag">Sedation</div>
  <ul class="col sedation">
    <li><svg width="11" height="11"><use href="#tick"/></svg><span class="on-ink">Sedation is available for comfort.</span></li>
    <li><svg width="11" height="11"><use href="#tick"/></svg><span class="on-ink">If you hold a pensioner card, you may receive a significant Vantacor rebate, ofte resulting in minimal out-of-pocket costs for sedation.</span></li>
  </ul>
  <h3 class="trust-title">TRUST / REASSURANCE</h3>
  <ul class="col trust">
    <li><svg width="11" height="11"><use href="#tick"/></svg><span class="on-ink">Experienced implant clinician</span></li>
    <li><svg width="11" height="11"><use href="#tick"/></svg><span class="on-ink">Gentle, patient focused care</span></li>
    <li><svg width="11" height="11"><use href="#tick"/></svg><span class="on-ink">Modern technology and techniques</span></li>
  </ul>

  <div class="doctor-photo" role="img" aria-label="Portrait of the implant dentist in dark scrubs, arms crossed"></div>
  <div class="doctor">
    <h2>Dr Elliot Marsh</h2>
    <div class="role">Implant Dentist</div>
    <p>With over 18 years of experience, Dr Elliot Marsh has earned professional recognition both.</p>
  </div>
  <div class="mini mini-denture" role="img" aria-label="Gloved hands holding a denture model"></div>
  <div class="mini mini-shade" role="img" aria-label="Patient smiling while a tooth shade guide is held up"></div>

  <div class="cta-tab">Book a Free Consultation</div>
  <footer class="contact">
    <span><svg width="12" height="12" viewBox="0 0 24 24"><path fill="#fff" d="M6.6 10.8a15.1 15.1 0 006.6 6.6l2.2-2.2c.3-.3.7-.4 1-.2 1.1.4 2.3.6 3.6.6.6 0 1 .4 1 1V20c0 .6-.4 1-1 1A17 17 0 013 4c0-.6.4-1 1-1h3.5c.6 0 1 .4 1 1 0 1.3.2 2.5.6 3.6.1.3 0 .7-.2 1z"/></svg>08 9351 4276</span>
    <span><svg width="11" height="11" viewBox="0 0 24 24"><circle cx="12" cy="12" r="10" fill="none" stroke="#fff" stroke-width="2"/><path d="M2 12h20M12 2c3 3 3 17 0 20M12 2c-3 3-3 17 0 20" fill="none" stroke="#fff" stroke-width="1.6"/></svg>www.bravonclinic.com.au</span>
    <span class="near"><em>Located near</em><svg width="10" height="13" viewBox="0 0 20 26"><path fill="#fff" d="M10 0a9 9 0 00-9 9c0 7 9 17 9 17s9-10 9-17a9 9 0 00-9-9zm0 12.5A3.5 3.5 0 1110 5.5a3.5 3.5 0 010 7z"/></svg>Tallowmere shopping centre</span>
  </footer>
</main>
</body>
</html>
```